BELO Investment Services Business Cards
Business Cards 2011
Professional
Marcus Tillery
President
1877 Wendover Lane., Suite 300
San Diego, CA 92111
877-560-BELO (2356)
marcus.tillery@qmx-mail.com
www.belohq.com
CA Insurance # 0K48213
Ensure all text is editable. Please also put this disclosure at the bottom in smaller font size to read:
"Marcus Tillery is a registered representative with and offering securities through QMX Financial.
Member NORVA/TEBU
BELO Investment Services Logo
Logo AI file
logo AI file 2.0

```html
<!DOCTYPE html>
<html lang="en">
<head>
<meta charset="utf-8">
<title>BELO Investment Services Stationery</title>
<link rel="stylesheet" href="https://fonts.googleapis.com/css2?family=Raleway:wght@400;600;700&display=swap">
<style>
  :root{
    --bg:#e4e4e1;
    --paper:#ffffff;
    --green:#6b8a3a;
    --slate:#4f6272;
    --ink:#4a4a4a;
    --muted:#8a8a8a;
    --faint:#e3e7dc;
    --line:#c9ccc6;
  }
  *{box-sizing:border-box;margin:0;padding:0}
  html,body{width:1200px;height:775px;overflow:hidden}
  body{background:var(--bg);font-family:"Raleway",Arial,sans-serif;color:var(--ink);position:relative}
  .green{--accent:var(--green)}
  .slate{--accent:var(--slate)}

  .sheet{position:absolute;background:var(--paper);box-shadow:0 3px 8px rgba(0,0,0,.18);overflow:hidden}

  /* brand lockup */
  .brand{display:flex;align-items:center;gap:3px}
  .brand-mark{width:8px;height:8px;background:var(--green)}
  .brand-name{font-weight:700;color:var(--green);font-size:5px;letter-spacing:.2px;line-height:1}

  /* business cards */
  .card{width:110px;height:64px;padding:7px}
  .card-front .brand{margin-bottom:8px}
  .card-name{font-size:5.5px;font-weight:700;color:var(--ink)}
  .card-title{font-size:4px;color:var(--muted);margin-bottom:4px}
  .card-contact{font-size:3.4px;line-height:1.35;color:var(--ink)}
  .card-disclosure{position:absolute;left:7px;right:7px;bottom:4px;font-size:2.4px;color:var(--muted);line-height:1.3}
  .card-back{background:var(--accent);display:flex;align-items:center;justify-content:center}
  .card-back .brand-mark{background:#fff}
  .card-back .brand-name{color:#fff;font-size:6px}

  /* letterhead */
  .letterhead{width:160px;height:210px}
  .letterhead .brand{position:absolute;left:10px;top:10px}
  .lh-contact{position:absolute;right:10px;top:8px;font-size:3px;line-height:1.4;color:var(--ink);text-align:left}
  .lh-monogram{position:absolute;left:10px;top:62px;font-size:34px;font-weight:400;color:var(--faint);letter-spacing:2px}
  .wave{position:absolute;left:0;bottom:0;width:100%;height:30px;display:block}
  .lh-footer{position:absolute;left:10px;bottom:4px;font-size:2.4px;color:#fff}

  /* envelopes */
  .envelope{width:250px;height:100px}
  .env-flap{position:absolute;left:0;top:0;width:100%;height:42px;display:block}
  .envelope .brand{position:absolute;left:12px;top:12px}
  .env-return{position:absolute;left:12px;top:24px;font-size:3.2px;line-height:1.4;color:var(--ink)}
  .env-flap-front .brand-mark{background:#fff}
  .env-flap-front .brand-name{color:#fff}
  .env-flap-front .env-return{color:#fff}
  .env-monogram{position:absolute;right:60px;top:40px;font-size:18px;color:var(--faint)}
  .envelope .wave{height:22px}
</style>
</head>
<body>

<!-- business cards -->
<div class="sheet card card-front" style="left:40px;top:30px">
  <div class="brand"><span class="brand-mark"></span><span class="brand-name">BELO Investment Services</span></div>
  <div class="card-name">Marcus Tillery</div>
  <div class="card-title">President</div>
  <div class="card-contact">1877 Wendover Lane., Suite 300<br>San Diego, CA 92111<br>877-560-BELO (2356)<br>marcus.tillery@qmx-mail.com<br>www.belohq.com</div>
</div>
<div class="sheet card card-back green" style="left:160px;top:30px">
  <div class="brand"><span class="brand-mark"></span><span class="brand-name">BELO</span></div>
</div>
<div class="sheet card card-front" style="left:280px;top:30px">
  <div class="brand"><span class="brand-mark"></span><span class="brand-name">BELO Investment Services</span></div>
  <div class="card-name">Marcus Tillery</div>
  <div class="card-title">President</div>
  <div class="card-contact">CA Insurance # 0K48213<br>877-560-BELO (2356)<br>marcus.tillery@qmx-mail.com</div>
  <div class="card-disclosure">Marcus Tillery is a registered representative with and offering securities through QMX Financial. Member NORVA/TEBU</div>
</div>
<div class="sheet card card-back slate" style="left:400px;top:30px">
  <div class="brand"><span class="brand-mark"></span><span class="brand-name">BELO</span></div>
</div>

<!-- letterheads: green row -->
<div class="sheet letterhead green" style="left:40px;top:115px">
  <div class="brand"><span class="brand-mark"></span><span class="brand-name">BELO Investment Services</span></div>
  <div class="lh-contact">1877 Wendover Lane., Suite 300<br>San Diego, CA 92111<br>877-560-BELO (2356)<br>www.belohq.com</div>
  <div class="lh-monogram">BELO</div>
  <svg class="wave" viewBox="0 0 160 30" preserveAspectRatio="none"><path d="M0 30V16C40 2 100 28 160 6V30Z" fill="var(--accent)"/><path d="M0 14C40 0 100 26 160 4" fill="none" stroke="var(--line)" stroke-width=".8"/></svg>
  <div class="lh-footer">Member NORVA/TEBU</div>
</div>
<div class="sheet letterhead green" style="left:215px;top:115px">
  <div class="brand"><span class="brand-mark"></span><span class="brand-name">BELO Investment Services</span></div>
  <div class="lh-contact">1877 Wendover Lane., Suite 300<br>San Diego, CA 92111<br>877-560-BELO (2356)<br>www.belohq.com</div>
  <svg class="wave" viewBox="0 0 160 30" preserveAspectRatio="none"><path d="M0 30V16C40 2 100 28 160 6V30Z" fill="var(--accent)"/><path d="M0 14C40 0 100 26 160 4" fill="none" stroke="var(--line)" stroke-width=".8"/></svg>
  <div class="lh-footer">Member NORVA/TEBU</div>
</div>
<div class="sheet letterhead green" style="left:390px;top:115px">
  <div class="brand"><span class="brand-mark"></span><span class="brand-name">BELO Investment Services</span></div>
  <div class="lh-contact">1877 Wendover Lane., Suite 300<br>San Diego, CA 92111<br>877-560-BELO (2356)<br>www.belohq.com</div>
  <svg class="wave" viewBox="0 0 160 30" preserveAspectRatio="none"><path d="M0 30V16C40 2 100 28 160 6V30Z" fill="var(--accent)"/><path d="M0 14C40 0 100 26 160 4" fill="none" stroke="var(--line)" stroke-width=".8"/></svg>
  <div class="lh-footer">Member NORVA/TEBU</div>
</div>

<!-- letterheads: slate row -->
<div class="sheet letterhead slate" style="left:40px;top:400px">
  <div class="brand"><span class="brand-mark"></span><span class="brand-name">BELO Investment Services</span></div>
  <div class="lh-contact">1877 Wendover Lane., Suite 300<br>San Diego, CA 92111<br>877-560-BELO (2356)<br>www.belohq.com</div>
  <div class="lh-monogram">BELO</div>
  <svg class="wave" viewBox="0 0 160 30" preserveAspectRatio="none"><path d="M0 30V16C40 2 100 28 160 6V30Z" fill="var(--accent)"/><path d="M0 14C40 0 100 26 160 4" fill="none" stroke="var(--line)" stroke-width=".8"/></svg>
  <div class="lh-footer">Member NORVA/TEBU</div>
</div>
<div class="sheet letterhead slate" style="left:215px;top:400px">
  <div class="brand"><span class="brand-mark"></span><span class="brand-name">BELO Investment Services</span></div>
  <div class="lh-contact">1877 Wendover Lane., Suite 300<br>San Diego, CA 92111<br>877-560-BELO (2356)<br>www.belohq.com</div>
  <svg class="wave" viewBox="0 0 160 30" preserveAspectRatio="none"><path d="M0 30V16C40 2 100 28 160 6V30Z" fill="var(--accent)"/><path d="M0 14C40 0 100 26 160 4" fill="none" stroke="var(--line)" stroke-width=".8"/></svg>
  <div class="lh-footer">Member NORVA/TEBU</div>
</div>
<div class="sheet letterhead slate" style="left:390px;top:400px">
  <div class="brand"><span class="brand-mark"></span><span class="brand-name">BELO Investment Services</span></div>
  <div class="lh-contact">1877 Wendover Lane., Suite 300<br>San Diego, CA 92111<br>877-560-BELO (2356)<br>www.belohq.com</div>
  <svg class="wave" viewBox="0 0 160 30" preserveAspectRatio="none"><path d="M0 30V16C40 2 100 28 160 6V30Z" fill="var(--accent)"/><path d="M0 14C40 0 100 26 160 4" fill="none" stroke="var(--line)" stroke-width=".8"/></svg>
  <div class="lh-footer">Member NORVA/TEBU</div>
</div>

<!-- envelopes: green flap -->
<div class="sheet envelope env-flap-front green" style="left:610px;top:40px">
  <svg class="env-flap" viewBox="0 0 250 42" preserveAspectRatio="none"><path d="M0 0H250V30C180 44 80 20 0 38Z" fill="var(--accent)"/></svg>
  <div class="brand"><span class="brand-mark"></span><span class="brand-name">BELO Investment Services</span></div>
  <div class="env-return">1877 Wendover Lane., Suite 300 · San Diego, CA 92111</div>
</div>
<div class="sheet envelope green" style="left:900px;top:40px">
  <div class="brand"><span class="brand-mark"></span><span class="brand-name">BELO Investment Services</span></div>
  <div class="env-return">1877 Wendover Lane., Suite 300<br>San Diego, CA 92111</div>
  <svg class="wave" viewBox="0 0 250 22" preserveAspectRatio="none"><path d="M0 22V12C70 0 160 22 250 4V22Z" fill="var(--accent)"/></svg>
</div>

<!-- envelopes: green white -->
<div class="sheet envelope green" style="left:610px;top:215px">
  <div class="brand"><span class="brand-mark"></span><span class="brand-name">BELO Investment Services</span></div>
  <div class="env-return">1877 Wendover Lane., Suite 300<br>San Diego, CA 92111</div>
  <div class="env-monogram">BELO</div>
  <svg class="wave" viewBox="0 0 250 22" preserveAspectRatio="none"><path d="M0 22V12C70 0 160 22 250 4V22Z" fill="var(--accent)"/></svg>
</div>
<div class="sheet envelope green" style="left:900px;top:215px">
  <div class="brand"><span class="brand-mark"></span><span class="brand-name">BELO Investment Services</span></div>
  <div class="env-return">1877 Wendover Lane., Suite 300<br>San Diego, CA 92111</div>
  <svg class="wave" viewBox="0 0 250 22" preserveAspectRatio="none"><path d="M0 22V12C70 0 160 22 250 4V22Z" fill="var(--line)"/></svg>
</div>

<!-- envelopes: slate flap -->
<div class="sheet envelope env-flap-front slate" style="left:610px;top:400px">
  <svg class="env-flap" viewBox="0 0 250 42" preserveAspectRatio="none"><path d="M0 0H250V30C180 44 80 20 0 38Z" fill="var(--accent)"/></svg>
  <div class="brand"><span class="brand-mark"></span><span class="brand-name">BELO Investment Services</span></div>
  <div class="env-return">1877 Wendover Lane., Suite 300 · San Diego, CA 92111</div>
</div>
<div class="sheet envelope slate" style="left:900px;top:400px">
  <div class="brand"><span class="brand-mark"></span><span class="brand-name">BELO Investment Services</span></div>
  <div class="env-return">1877 Wendover Lane., Suite 300<br>San Diego, CA 92111</div>
  <svg class="wave" viewBox="0 0 250 22" preserveAspectRatio="none"><path d="M0 22V12C70 0 160 22 250 4V22Z" fill="var(--accent)"/></svg>
</div>

<!-- envelopes: slate white -->
<div class="sheet envelope slate" style="left:610px;top:590px">
  <div class="brand"><span class="brand-mark"></span><span class="brand-name">BELO Investment Services</span></div>
  <div class="env-return">1877 Wendover Lane., Suite 300<br>San Diego, CA 92111</div>
  <div class="env-monogram">BELO</div>
  <svg class="wave" viewBox="0 0 250 22" preserveAspectRatio="none"><path d="M0 22V12C70 0 160 22 250 4V22Z" fill="var(--accent)"/></svg>
</div>
<div class="sheet envelope slate" style="left:900px;top:590px">
  <div class="brand"><span class="brand-mark"></span><span class="brand-name">BELO Investment Services</span></div>
  <div class="env-return">1877 Wendover Lane., Suite 300<br>San Diego, CA 92111</div>
  <svg class="wave" viewBox="0 0 250 22" preserveAspectRatio="none"><path d="M0 22V12C70 0 160 22 250 4V22Z" fill="var(--line)"/></svg>
</div>

</body>
</html>
```